Kick Ass, Edgy, Fun, E commerce Embroidery Company Business Card

Sleek and edgy business card layout. main logo on front with business description (Custom Embroidery, the file is submitted is supposed to look like stitching)
Name, address, phone numbers, social icons (Facebook and Instagram) on back. The card will be black plastic and the front main logo will be printed Spot UV.

Target Market(s)

Small Business Owners

Contact Information for Business Card

Focused, not cluttered and sleek. Modern looking.

Font styles to use
Other font styles liked:
• Very clean and elegant

Colors
acd136

Requirements
Must have
• Custom Embroidery

our Tagline: Every Logo Has A Story - Thread Yours
Nice to have
• Social Icons for Facebook and Instagram
Should not have
• Too much visual noise

```html
<!DOCTYPE html>
<html lang="en">
<head>
<meta charset="utf-8">
<title>StitchForge Inc – Business Card</title>
<link rel="stylesheet" href="https://fonts.googleapis.com/css2?family=Arimo:wght@400;700&display=swap">
<style>
  :root {
    --card-black: #050708;
    --accent-lime: #acd136;
    --text-white: #ffffff;
    --page-bg: #ffffff;
  }
  html, body {
    margin: 0;
    padding: 0;
    width: 1200px;
    height: 749px;
    overflow: hidden;
    background: var(--page-bg);
  }
  .card {
    position: relative;
    width: 1200px;
    height: 749px;
    background: var(--card-black);
    border-radius: 46px;
    overflow: hidden;
    font-family: "Arimo", Arial, sans-serif;
    color: var(--text-white);
  }
  .side-band {
    position: absolute;
    top: 208px;
    height: 327px;
    background: var(--accent-lime);
  }
  .side-band--left { left: 0; width: 97px; }
  .side-band--right { left: 1105px; width: 95px; }

  .brand {
    position: absolute;
    left: 280px;
    top: 208px;
    width: 296px;
    height: 327px;
    text-align: center;
  }
  .brand-dot {
    position: absolute;
    left: 88px;
    top: 30px;
    width: 120px;
    height: 120px;
    border-radius: 50%;
    background: var(--text-white);
  }
  .brand-name {
    position: absolute;
    left: 0;
    right: 0;
    top: 214px;
    margin: 0;
    font-weight: 700;
    font-size: 56px;
    line-height: 58px;
    letter-spacing: 1px;
    color: var(--text-white);
  }

  .divider {
    position: absolute;
    left: 595px;
    top: 208px;
    width: 3px;
    height: 327px;
    background: var(--text-white);
  }

  .details {
    position: absolute;
    left: 628px;
    top: 212px;
  }
  .company-name {
    margin: 0;
    font-weight: 700;
    font-size: 44px;
    line-height: 56px;
    color: var(--accent-lime);
  }
  .address {
    margin: 0;
    font-style: normal;
    font-size: 30px;
    line-height: 46px;
  }
  .contact-list {
    list-style: none;
    margin: 44px 0 0 0;
    padding: 0;
  }
  .contact-item {
    display: flex;
    align-items: center;
    height: 46px;
    font-size: 30px;
  }
  .contact-icon {
    width: 30px;
    height: 30px;
    margin-right: 14px;
    flex: none;
  }
  .social-list {
    position: absolute;
    left: 637px;
    top: 583px;
    display: flex;
    gap: 39px;
    margin: 0;
    padding: 0;
    list-style: none;
  }
  .social-slot {
    width: 49px;
    height: 44px;
    border: 2.5px solid var(--accent-lime);
    border-radius: 10px;
    box-sizing: border-box;
  }
</style>
</head>
<body>
<main class="card">
  <div class="side-band side-band--left"></div>
  <div class="side-band side-band--right"></div>

  <div class="brand">
    <div class="brand-dot"></div>
    <p class="brand-name">STITCH<br>FORGE</p>
  </div>

  <div class="divider"></div>

  <section class="details">
    <h1 class="company-name">StitchForge Inc</h1>
    <address class="address">4417 Meadow Ridge Dr Ste 5<br>Aurora, CO 80016</address>
    <ul class="contact-list">
      <li class="contact-item">
        <svg class="contact-icon" viewBox="0 0 30 30" aria-hidden="true">
          <rect x="9" y="3" width="13" height="24" rx="2.5" fill="none" stroke="#acd136" stroke-width="2.4"/>
          <circle cx="15.5" cy="23" r="1.4" fill="#acd136"/>
        </svg>
        1-800-555-0147
      </li>
      <li class="contact-item">
        <svg class="contact-icon" viewBox="0 0 30 30" aria-hidden="true">
          <rect x="1" y="7" width="28" height="18" fill="#acd136"/>
          <polyline points="1,7 15,18 29,7" fill="none" stroke="#050708" stroke-width="2"/>
        </svg>
        info@StitchForge.com
      </li>
      <li class="contact-item">
        <svg class="contact-icon" viewBox="0 0 30 30" aria-hidden="true">
          <circle cx="15" cy="15" r="12" fill="none" stroke="#acd136" stroke-width="2.4"/>
          <ellipse cx="15" cy="15" rx="5" ry="12" fill="none" stroke="#acd136" stroke-width="2"/>
          <line x1="3" y1="15" x2="27" y2="15" stroke="#acd136" stroke-width="2"/>
        </svg>
        StitchForge.com
      </li>
    </ul>
  </section>

  <ul class="social-list">
    <li class="social-slot" aria-label="Social profile"></li>
    <li class="social-slot" aria-label="Social profile"></li>
  </ul>
</main>
</body>
</html>
```